Professional business cards for real estate development company

I need business cards for my new real estate development company. The company, "KORVA" is a real estate development, investment, and advisory firm with a focus on multifamily, office, and mixed-use projects across primary and secondary markets in the Southeast United States.

Style preference is modern

Industry/Entity Type

Real Estate Development

Contact Information for Business Card

The business cards need to include:
Name
Title
Mailing Address
Phone Number
Web Address

Logo is attached. I would like white to be the primary color with incorporation of the company colors: #232D3A and #B5A451

Font styles to use
Other font styles liked:
• Montserrat, Avenir

Requirements
Must have
• Company Logo. No need to include the company name since the name is in the logo.
Should not have
• No line type designs

```html
<!DOCTYPE html>
<html lang="en">
<head>
<meta charset="UTF-8">
<title>KORVA Business Cards</title>
<link href="https://fonts.googleapis.com/css2?family=Poppins:wght@400;500;600;700&display=swap" rel="stylesheet">
<style>
  :root {
    --backdrop: #1b1c1f;
    --card: #ffffff;
    --ink: #232d3a;
    --ink-soft: #2f3947;
  }
  * { margin: 0; padding: 0; box-sizing: border-box; }
  html, body {
    width: 1200px;
    height: 1200px;
    overflow: hidden;
    background: var(--backdrop);
    font-family: "Poppins", sans-serif;
    color: var(--ink);
  }
  .stage {
    width: 1200px;
    height: 1200px;
    display: flex;
    flex-direction: column;
    align-items: center;
    justify-content: center;
    gap: 70px;
  }
  .card {
    width: 780px;
    height: 446px;
    background: var(--card);
    position: relative;
    box-shadow: 0 12px 30px rgba(0,0,0,0.45);
  }
  /* Front */
  .card-front {
    display: flex;
    flex-direction: column;
    align-items: center;
    justify-content: center;
  }
  .brand-name {
    font-weight: 600;
    font-size: 96px;
    letter-spacing: 0.04em;
    line-height: 1;
    color: var(--ink);
  }
  .front-web {
    margin-top: 48px;
    font-size: 19px;
    font-weight: 400;
    letter-spacing: 0.42em;
    color: var(--ink-soft);
  }
  /* Back */
  .card-back {
    display: flex;
    align-items: center;
    justify-content: center;
  }
  .person {
    width: 330px;
    text-align: right;
    padding-right: 34px;
    align-self: center;
    margin-top: -30px;
  }
  .person-name {
    font-weight: 700;
    font-size: 28px;
    letter-spacing: 0.02em;
    line-height: 1.1;
    text-transform: uppercase;
  }
  .person-title {
    font-size: 20px;
    font-weight: 400;
    color: var(--ink-soft);
  }
  .divider {
    width: 2px;
    height: 150px;
    background: var(--ink);
  }
  .contact {
    width: 400px;
    padding-left: 40px;
    font-size: 21px;
    line-height: 1.25;
  }
  .address { margin-bottom: 14px; }
  .contact-list { list-style: none; }
  .contact-item {
    display: flex;
    align-items: center;
    gap: 12px;
    margin-bottom: 2px;
  }
  .contact-icon {
    width: 22px;
    height: 22px;
    flex: none;
  }
</style>
</head>
<body>
<main class="stage">
  <section class="card card-front" aria-label="Card front">
    <div class="brand-name">KORVA</div>
    <div class="front-web">www.korvadev.com</div>
  </section>

  <section class="card card-back" aria-label="Card back">
    <div class="person">
      <div class="person-name">Daniel R. Hayes</div>
      <div class="person-title">Executive Director</div>
    </div>
    <div class="divider"></div>
    <div class="contact">
      <p class="address">PO BOX 418 Harbor Lane<br>2nd street Raleigh, USA</p>
      <ul class="contact-list">
        <li class="contact-item">
          <svg class="contact-icon" viewBox="0 0 22 22" aria-hidden="true">
            <circle cx="11" cy="11" r="11" fill="#232d3a"/>
            <path d="M8 6.5c.6-.4 1.2-.2 1.5.4l.6 1.4c.2.5 0 1-.4 1.3l-.5.4c.5 1.2 1.4 2.1 2.6 2.6l.4-.5c.3-.4.8-.6 1.3-.4l1.4.6c.6.3.8.9.4 1.5-.6.9-1.6 1.3-2.6.9-2.5-1-4.4-2.9-5.4-5.4-.4-1 0-2 .7-2.8z" fill="#fff"/>
          </svg>
          <span>555-204-3187</span>
        </li>
        <li class="contact-item">
          <svg class="contact-icon" viewBox="0 0 22 22" aria-hidden="true">
            <circle cx="11" cy="11" r="11" fill="#232d3a"/>
            <rect x="5.5" y="7" width="11" height="8" rx="1" fill="none" stroke="#fff" stroke-width="1.4"/>
            <path d="M5.8 7.5 11 11.5l5.2-4" fill="none" stroke="#fff" stroke-width="1.4"/>
          </svg>
          <span>hello@korvadev.com</span>
        </li>
        <li class="contact-item">
          <svg class="contact-icon" viewBox="0 0 22 22" aria-hidden="true">
            <circle cx="11" cy="11" r="11" fill="#232d3a"/>
            <circle cx="11" cy="11" r="5.5" fill="none" stroke="#fff" stroke-width="1.2"/>
            <ellipse cx="11" cy="11" rx="2.4" ry="5.5" fill="none" stroke="#fff" stroke-width="1.1"/>
            <path d="M5.5 11h11M6.4 8h9.2M6.4 14h9.2" stroke="#fff" stroke-width="1"/>
          </svg>
          <span>www.korvadev.com</span>
        </li>
      </ul>
    </div>
  </section>
</main>
</body>
</html>
```